Ad Template Needed for Postboardly PLEASE!

Hi, I need a professional designer who can design a template for real estate ads for Postboardly.
The ads I am currently running are OK, but I need them to have a bit more of a professional polish.
Here is what I need:
The ads must direct people to click my "questionnaire", this is a short survey that is completed off site.
The ads should also entice the viewer to contact me thought email or phone.
PLEASE NO COOKIE-CUTTER ADS!. No stock photos, or generic content. These must be original.
I have attached the html for my previous ads. Please provide previous work if you apply for the job.
Here are links to some the actual ads I am currently running, these are a good base, but I need them to be improved. You would be redesigning these:
http://metro.postboardly-example.net/lst/apt/8120934411.html
http://metro.postboardly-example.net/lst/apt/8120934276.html
http://metro.postboardly-example.net/lst/apt/8120905521.html
http://metro.postboardly-example.net/lst/apt/8120876302.html
IMPORTANT PLEASE READ:
You will not have to do anything with the photos in the ads, I can change these out as needed.
You do not need to worry about content, meaning wording.
These ads MUST be full width.
I will need these coded to HTML, not sure if that is feasible with my budget, it not please let me know.
Let me know if you have any questions, thank you.
Real Estate

```html
<!DOCTYPE html>
<html lang="en">
<head>
<meta charset="utf-8">
<title>Castell Properties – Listing Ad</title>
<link href="https://fonts.googleapis.com/css2?family=Arimo:wght@400;700&display=swap" rel="stylesheet">
<style>
:root{
  --brand-red:#a50d0d;
  --ink:#111111;
  --band-grey:#e6e6e6;
  --rule:#cfcfcf;
  --link-blue:#2a55d4;
  --pill-blue:#d9e8f2;
  --photo-warm:#d9d2c8;
  --photo-sky:#c9d4de;
}
*{box-sizing:border-box;margin:0;padding:0}
html,body{width:898px;height:1200px;overflow:hidden;background:#fff}
body{font-family:"Arimo",Arial,sans-serif;color:var(--ink);position:relative}
.top-rule{position:absolute;left:0;top:4px;width:100%;height:1px;background:var(--rule)}
.brand{position:absolute;left:0;top:0;width:100%;height:115px;display:flex;align-items:center;justify-content:center}
.brand-name{font-size:38px;font-weight:400;letter-spacing:4px;color:var(--brand-red);white-space:nowrap}
.agent-band{position:absolute;left:0;top:115px;width:100%;height:205px;background:var(--band-grey);border-top:1px solid var(--rule);border-bottom:1px solid var(--rule)}
.agent-photo{position:absolute;left:257px;top:9px;width:157px;height:188px;border:1px solid var(--brand-red);background:linear-gradient(180deg,#f4f4f4 0%,#e8ddd6 45%,#2b2b2e 75%,#1c1c1f 100%)}
.agent-card{position:absolute;left:414px;top:39px;width:268px;height:137px;background:#fff}
.agent-name{height:47px;background:var(--brand-red);color:#fff;font-weight:700;font-size:29px;display:flex;align-items:center;justify-content:center;white-space:nowrap}
.agent-phone{display:flex;align-items:center;justify-content:center;gap:10px;margin:12px auto 0;width:186px;padding-bottom:6px;border-bottom:1px solid var(--ink);font-size:23px;white-space:nowrap}
.agent-phone svg{flex:none}
.agent-title{text-align:center;font-weight:700;font-size:12px;letter-spacing:1px;margin-top:14px;white-space:nowrap}
.email-row{position:absolute;left:0;top:320px;width:100%;height:47px;border-bottom:1px solid var(--rule);display:flex;align-items:center;justify-content:center;gap:14px}
.email-row a{color:var(--link-blue);text-decoration:none;font-size:21px}
.kicker{position:absolute;top:393px;width:100%;text-align:center;font-weight:700;font-size:13px}
.listing{position:absolute;left:129px;top:429px;width:660px}
.listing h1{font-size:16px;font-weight:700;margin-bottom:10px}
.listing p{font-size:12.5px;line-height:22px}
.credit{position:absolute;top:526px;width:100%;text-align:center;color:var(--brand-red);font-size:12px}
.listing-photo{position:absolute;left:122px;top:551px;width:635px;height:424px;background:linear-gradient(90deg,var(--photo-warm) 0%,#e6e2dc 30%,var(--photo-sky) 70%,#aab7c2 100%)}
.cta-lead{position:absolute;top:1007px;width:100%;text-align:center;font-weight:700;font-size:16.5px}
.cta-pill{position:absolute;left:212px;top:1041px;width:475px;height:55px;border-radius:28px;background:var(--pill-blue);display:flex;align-items:center;padding-left:20px;gap:14px;font-weight:700;font-size:16.5px;text-decoration:none;color:var(--ink);white-space:nowrap}
.cta-pill span{color:var(--link-blue)}
.footer{position:absolute;left:0;top:1129px;width:100%;height:71px;background:var(--band-grey);border-top:1px solid var(--rule);text-align:center;font-size:9.5px;padding-top:16px;line-height:15px}
.footer a{color:var(--link-blue);text-decoration:none}
</style>
</head>
<body>
<div class="top-rule"></div>
<header class="brand">
  <div class="brand-name">Castell Properties</div>
</header>

<section class="agent-band">
  <div class="agent-photo" role="img" aria-label="Portrait photo of the agent"></div>
  <div class="agent-card">
    <div class="agent-name">DANIEL ROURKE</div>
    <div class="agent-phone">
      <svg width="14" height="22" viewBox="0 0 14 22" aria-hidden="true"><rect x="0" y="0" width="14" height="22" rx="1" fill="var(--brand-red)"/><rect x="2.5" y="2.5" width="9" height="7" fill="#fff"/><g fill="#fff"><rect x="2.5" y="12" width="2" height="2"/><rect x="6" y="12" width="2" height="2"/><rect x="9.5" y="12" width="2" height="2"/><rect x="2.5" y="16" width="2" height="2"/><rect x="6" y="16" width="2" height="2"/><rect x="9.5" y="16" width="2" height="2"/></g></svg>
      <span>347-555-0182</span>
    </div>
    <div class="agent-title">YOUR FIDI SPECIALIST</div>
  </div>
</section>

<div class="email-row">
  <svg width="26" height="17" viewBox="0 0 26 17" aria-hidden="true"><rect width="26" height="17" fill="var(--brand-red)"/><path d="M1 1 L13 10 L25 1" fill="none" stroke="#fff" stroke-width="1.6"/></svg>
  <a href="mailto:daniel@castellproperties.com">daniel@castellproperties.com</a>
</div>

<div class="kicker">~BRAND NEW TO MARKET~</div>

<article class="listing">
  <h1>Stunning Fi-Di Luxury Building!</h1>
  <p>This apartment has <b>great light, space, and storage</b>. Enjoy free amenities in a full service doorman building.<br>The unit comes with brand new stainless steel appliances and a 1 year old renovated kitchen and bathroom.</p>
</article>

<div class="credit">Daniel Rourke | Licensed Salesperson | Castell Properties (347) 555-0182</div>

<div class="listing-photo" role="img" aria-label="Listing photo: bright living room with sofa and floor-to-ceiling windows over the harbor"></div>

<div class="cta-lead">Looking for something else? No Problem.</div>
<a class="cta-pill" href="#questionnaire">
  <svg width="44" height="44" viewBox="0 0 44 44" aria-hidden="true"><path d="M22 3a19 19 0 1 0 8 36l7 4-2-8A19 19 0 0 0 22 3z" fill="var(--brand-red)"/><text x="22" y="31" text-anchor="middle" font-family="Arimo,Arial,sans-serif" font-weight="700" font-size="26" fill="#fff">?</text></svg>
  <div><span>Click here</span> to Fill out my 60 second Questionnaire</div>
</a>

<footer class="footer">
  © 2012 Castell Properties<br>
  <a href="#">terms of use</a> | <a href="#">privacy</a> | <a href="#">feedback</a>
</footer>
</body>
</html>
```